Adult Literacy Program - flyer to attract volunteers and students

We want a flyer that is engaging, colorful, modern and will appeal to our primary audience of adults aged 40-60. We are trying to attract both prospective volunteers (typically age 50+, mostly women) and students (typically aged 40+).
The flyer should feature diverse people working together in pairs of two, reading or talking, with a workbook or some reading material in front of them.

Our organization trains tutors to work one-on-one with adults who are learning how to read. Most of our adult students are non-native speakers of English. Many are of Haitian or Hispanic origin, so we would like some people who represent that demographic.

The Flyer should represent reading, learning, literacy, knowledge, growth,
and opportunities.
Our students are learning to read so they can advance their job opportunities.

Target Market(s)

Adults aged 40-60, primarily women, retired, volunteers

Industry/Entity Type

Education

Font styles to use
Serif
Sans Serif

Colors

Designer to choose colors to be used in the design.

Requirements
Must have
• - UPDATE: Should be designed as a TRI-FOLD brochure on 8.5 x 11 inch paper that will be folded into thirds.
• - Images of diverse people, women and men, who look Hispanic, Haitian and other nationalities as well as Caucasian.
• - Our logo on the front cover
Nice to have
• The sample flyer is very boring and dry! We are open to different ways of presenting the text.

```html
<!DOCTYPE html>
<html lang="en">
<head>
<meta charset="utf-8">
<title>Adult Literacy Program – Tri-fold Inside</title>
<link rel="stylesheet" href="https://fonts.googleapis.com/css2?family=Arimo:wght@400;700&family=Roboto+Condensed:wght@400&family=Varela+Round&display=swap">
<style>
  :root {
    --magenta: #c8095c;
    --cyan: #86d3e4;
    --grey-light: #e2e2e4;
    --grey-mid: #d2d2d4;
    --ink: #2e2e30;
    --caption: #6a6a6e;
    --white: #ffffff;
  }
  * { margin: 0; padding: 0; box-sizing: border-box; }
  html, body { width: 1200px; height: 865px; overflow: hidden; background: var(--white); }
  .spread { position: relative; width: 1200px; height: 865px; font-family: "Arimo", Arial, sans-serif; color: var(--ink); }
  .block { position: absolute; }

  .page-bg { left: 28px; top: 29px; width: 1144px; height: 807px; background: var(--grey-light); }
  .panel-mid-bg { left: 413px; top: 29px; width: 382px; height: 807px; background: var(--grey-mid); }
  .top-rule { left: 28px; top: 38px; width: 767px; height: 9px; background: var(--magenta); }

  .photo { position: absolute; }
  .photo--conversation { left: 28px; top: 47px; width: 431px; height: 272px;
    background: linear-gradient(120deg, #e9b7c8 0%, #b77d98 45%, #5b3a55 100%); }
  .photo--reader { left: 413px; top: 572px; width: 759px; height: 217px;
    background: linear-gradient(100deg, #e8e2da 0%, #cdbfae 35%, #a07a5c 65%, #3a3032 100%); }

  .bottom-rule { left: 413px; top: 789px; width: 759px; height: 10px; background: var(--magenta); }

  .heading { position: absolute; font-family: "Varela Round", "Arial Rounded MT Bold", sans-serif;
    color: var(--magenta); font-size: 24px; letter-spacing: 0.5px; }
  .heading--tutor { left: 75px; top: 357px; }
  .heading--students { left: 486px; top: 151px; }

  .list { position: absolute; list-style: none; font-size: 16.5px; line-height: 21px; }
  .list > li { position: relative; padding-left: 20px; margin-bottom: 12px; }
  .list > li::before { content: ""; position: absolute; left: 1px; top: 7px; width: 7px; height: 7px;
    border-radius: 50%; background: var(--ink); }
  .list--tutor { left: 77px; top: 402px; width: 280px; }
  .list--students { left: 488px; top: 190px; width: 300px; }
  .list--students > li { margin-bottom: 8px; }
  .sublist { list-style: none; font-size: 15px; line-height: 21px; margin-top: 2px; }
  .sublist li { position: relative; padding-left: 14px; }
  .sublist li::before { content: ""; position: absolute; left: 0; top: 10px; width: 8px; height: 3px; background: var(--ink); }
  .small { font-size: 15px; }

  .callout { position: absolute; display: flex; align-items: center; justify-content: center; text-align: center;
    font-family: "Varela Round", "Arial Rounded MT Bold", sans-serif; color: var(--white);
    font-size: 17.5px; line-height: 24px; letter-spacing: 1.2px; word-spacing: 3px; }
  .callout--teach { left: 28px; top: 669px; width: 385px; height: 120px; background: var(--cyan); }
  .callout--read { left: 413px; top: 452px; width: 382px; height: 120px; background: var(--magenta); padding-bottom: 6px; }

  .activities-header { position: absolute; left: 795px; top: 29px; width: 377px; height: 102px; background: var(--cyan); }
  .activities-title { position: absolute; left: 809px; top: 98px; font-family: "Varela Round", sans-serif;
    font-size: 20px; color: var(--white); letter-spacing: 1px; word-spacing: 4px; }

  .thumb { position: absolute; border: 3px solid var(--cyan); }
  .thumb__num { position: absolute; top: 5px; right: 5px; width: 15px; height: 15px; border-radius: 50%;
    background: rgba(255,255,255,0.85); color: var(--caption); font-family: "Arimo", sans-serif;
    font-size: 10px; font-weight: 700; line-height: 15px; text-align: center; }
  .thumb--training { left: 812px; top: 164px; width: 195px; height: 136px;
    background: linear-gradient(160deg, #c9c4b8 0%, #8f887b 60%, #4d4944 100%); }
  .thumb--one-on-one { left: 1015px; top: 164px; width: 139px; height: 136px;
    background: linear-gradient(135deg, #b07b4d 0%, #6fc2bf 50%, #e8e6c9 100%); }
  .thumb--pair { left: 812px; top: 308px; width: 133px; height: 137px;
    background: linear-gradient(135deg, #d6b25d 0%, #8a3d3a 50%, #7aa0d4 100%); }
  .thumb--group { left: 959px; top: 308px; width: 195px; height: 137px;
    background: linear-gradient(160deg, #a8cf5e 0%, #c4b28a 55%, #6e5e52 100%); }

  .captions { position: absolute; left: 818px; top: 457px; list-style: none;
    font-family: "Roboto Condensed", "Arial Narrow", sans-serif; font-size: 12.5px; line-height: 18.5px; color: var(--caption); }
</style>
</head>
<body>
<div class="spread">
  <div class="block page-bg"></div>
  <div class="block panel-mid-bg"></div>
  <div class="block top-rule"></div>

  <!-- Panel: tutor -->
  <div class="photo photo--conversation" role="img" aria-label="Photo of two women talking across a small round table by a city window"></div>
  <h2 class="heading heading--tutor">TUTOR</h2>
  <ul class="list list--tutor">
    <li>No special skills or degrees needed &nbsp;— just a degree of caring!</li>
    <li>Training offered throughout the year</li>
    <li>Tutors meet students weekly at a library</li>
    <li>Instructional materials provided</li>
    <li>Ongoing support available</li>
  </ul>
  <p class="callout callout--teach">Teach an adult to read<br>and you'll change a life forever.</p>

  <!-- Panel: students -->
  <h2 class="heading heading--students">STUDENTS</h2>
  <ul class="list list--students">
    <li>Students are adults in need of:
      <ul class="sublist">
        <li>basic literacy skills</li>
        <li>pre-GED skills</li>
        <li>conversational English</li>
      </ul>
    </li>
    <li>Tutoring is free of charge</li>
    <li>Tutoring is one-on-one</li>
    <li>Flexible scheduling during<br><span class="small">library hours</span></li>
    <li>Lessons focus on student goals</li>
  </ul>
  <p class="callout callout--read">If you can read,<br>you can tutor!</p>

  <!-- Panel: activities -->
  <div class="activities-header"></div>
  <h2 class="activities-title">OUR ACTIVITIES</h2>
  <div class="thumb thumb--training" role="img" aria-label="Photo of a tutor training session in a meeting room"><span class="thumb__num">1</span></div>
  <div class="thumb thumb--one-on-one" role="img" aria-label="Photo of a tutor and student working together over a workbook"><span class="thumb__num">2</span></div>
  <div class="thumb thumb--pair" role="img" aria-label="Photo of a smiling student standing with her tutor"><span class="thumb__num">4</span></div>
  <div class="thumb thumb--group" role="img" aria-label="Photo of a group training around tables in a bright room"><span class="thumb__num">3</span></div>
  <ol class="captions">
    <li>1. Tutor training</li>
    <li>2. One-on-on tutoring</li>
    <li>3. Training offered throughout the year</li>
    <li>4. A student and her tutor</li>
  </ol>

  <div class="photo photo--reader" role="img" aria-label="Photo of hands holding an open book while reading"></div>
  <div class="block bottom-rule"></div>
</div>
</body>
</html>
```